Book Cover Design Project

I need a book cover design with the title

"Hollow Vault - A Journey past Shadows and Schemes behind Norvania’s $4 Billion Retirement Savings Trade"

With a question on the cover of "How much of your superannuation has been stolen? Read this Book to Find Out"

The design should have money and greed based theme such as "$" for "S" in "Super"

Target Market(s)

Members of Superannuation (Pension) funds

Industry/Entity Type

Industry

Requirements
Must have
• Must have a money and greed theme

```html
<!DOCTYPE html>
<html lang="en">
<head>
<meta charset="utf-8">
<title>Hollow Vault – Book Cover</title>
<link rel="stylesheet" href="https://fonts.googleapis.com/css2?family=Bebas+Neue&family=Arimo:wght@400&display=swap">
<style>
  :root {
    --backdrop: #e4e4e4;
    --cover-black: #000000;
    --gold: #f0b81a;
    --white: #ffffff;
    --flame: #e8741c;
    --skin: #b07a56;
  }
  html, body {
    margin: 0;
    padding: 0;
    width: 1200px;
    height: 801px;
    overflow: hidden;
    background: var(--backdrop);
  }
  .book-cover {
    position: absolute;
    left: 380px;
    top: 60px;
    width: 440px;
    height: 684px;
    display: block;
  }
  .display-type {
    font-family: "Bebas Neue", "Oswald", sans-serif;
  }
  .author-name {
    font-size: 34px;
    letter-spacing: 7px;
    fill: var(--white);
  }
  .title-gold { fill: var(--gold); }
  .title-white { fill: var(--white); }
  .tagline {
    font-family: "Arimo", Arial, sans-serif;
    fill: var(--white);
  }
</style>
</head>
<body>
<svg class="book-cover" viewBox="0 0 440 684" xmlns="http://www.w3.org/2000/svg">
  <defs>
    <radialGradient id="hero-glow" cx="50%" cy="40%" r="55%">
      <stop offset="0%" stop-color="var(--flame)"/>
      <stop offset="45%" stop-color="#6b3a1c"/>
      <stop offset="100%" stop-color="var(--cover-black)"/>
    </radialGradient>
  </defs>

  <rect class="cover-base" x="0" y="0" width="440" height="684" fill="var(--cover-black)"/>

  <text class="display-type author-name" x="220" y="36" text-anchor="middle">AUTHOR NAME</text>
  <rect class="author-rule" x="84" y="44" width="272" height="2" fill="var(--white)"/>

  <rect class="hero-image" x="120" y="56" width="200" height="230" fill="url(#hero-glow)"
        role="img" aria-label="A clenched fist holding a wad of banknotes that are on fire"/>

  <g class="display-type book-title">
    <text class="title-gold" x="20" y="344" font-size="68" textLength="400" lengthAdjust="spacingAndGlyphs">HOLLOW VAULT</text>
    <text class="title-white" x="40" y="400" font-size="56" textLength="360" lengthAdjust="spacingAndGlyphs">-A JOURNEY PAST</text>
    <text class="title-gold" x="80" y="440" font-size="38" textLength="280" lengthAdjust="spacingAndGlyphs">SHADOWS AND SCHEMES</text>
    <text class="title-white" x="20" y="504" font-size="62" textLength="400" lengthAdjust="spacingAndGlyphs">BEHIND NORVANIA’S</text>
    <text class="title-gold" x="20" y="564" font-size="64" textLength="400" lengthAdjust="spacingAndGlyphs">$4 BILLION</text>
    <text class="title-white" x="72" y="600" font-size="32" textLength="296" lengthAdjust="spacingAndGlyphs">RETIREMENT SAVINGS TRADE</text>
  </g>

  <rect class="tagline-rule" x="4" y="626" width="432" height="3" fill="var(--gold)"/>

  <text class="tagline tagline-question" x="220" y="648" font-size="15" text-anchor="middle">How much of your superannuation has been stolen?</text>
  <text class="tagline tagline-call" x="220" y="675" font-size="25" text-anchor="middle">Read this Book to Find Out</text>
</svg>
</body>
</html>
```